Tri-fold Brochure Design for Law Firm

I need a tri-fold brochure to give to prospective clients.
I have attached a Photoshop design file of a tri-fold brochure. The content (copy) is good, however, he brochure itself looks very amateurish.
I want a professional, sophisticated looking brochure.
The law firm specializes in commercial debt collection.
The law firm is located in New York City.
Our target market is business owners, doctors, lawyers, collection agencies and accountants.
Visit my website which is being designed at www.dorvenlaw.com. I like the font used for the name of my company and the rich blue color used.

Target Market(s)

Business Owners, Doctors, Law Firms and Accountants

Industry/Entity Type

Law Firm

Font styles to use
Serif

Requirements
Must have
• Professional quality graphic work. Attention to details.
• PHOTOGRAPHS ONLY, NO CLIP-ART.
• DARK COLORS - NAVY BLUE, HUNTER GREEN, BLACK, GRAY & WHITE
Nice to have
• I want it to look smart, modern and sophisticated.
• Visit my website which is being designed at www.dorvenlaw.com. I like the font used for the name of my company and the rich blue color used.
Should not have
• Bad artwork
• CLIP ART

```html
<!DOCTYPE html>
<html lang="en">
<head>
<meta charset="utf-8">
<title>Marcus Dorven &amp; Company – Tri-fold Brochure</title>
<link rel="stylesheet" href="https://fonts.googleapis.com/css2?family=Cinzel:wght@600&family=Open+Sans:wght@400;600;700&family=Saira+Condensed:wght@600&display=swap">
<style>
  :root {
    --royal: #2e3192;
    --ink: #1f1f21;
    --charcoal: #3a3a3c;
    --paper: #ffffff;
    --text: #222226;
    --backdrop: #e6e6e6;
    --fold: #e2e2e6;
    --serif: "Cinzel", Georgia, serif;
    --head: "Saira Condensed", "Arial Narrow", sans-serif;
    --body: "Open Sans", Arial, sans-serif;
  }
  * { box-sizing: border-box; margin: 0; padding: 0; }
  html, body { width: 1200px; height: 960px; overflow: hidden; }
  body { background: var(--backdrop); position: relative; font-family: var(--body); color: var(--text); }

  .spread { position: absolute; left: 20px; width: 1160px; height: 455px; background: var(--paper); box-shadow: 0 2px 10px rgba(0,0,0,.15); overflow: hidden; }
  .spread--outside { top: 20px; }
  .spread--inside { top: 490px; }
  .spread > svg.shapes { position: absolute; inset: 0; }
  .block { position: absolute; }

  .heading { font-family: var(--head); font-weight: 600; color: var(--royal); text-transform: uppercase; letter-spacing: .5px; line-height: 1; }
  p { font-size: 8.5px; line-height: 1.32; margin-bottom: 3px; text-align: justify; }

  /* outside */
  .partner { left: 22px; top: 14px; width: 350px; }
  .partner .heading { font-size: 21px; margin-bottom: 5px; }
  .partner p { font-size: 9.5px; line-height: 1.33; }
  .serve-title { font-size: 10px; color: var(--royal); font-weight: 600; margin: 4px 0 2px; }
  .serve-list { list-style: none; columns: 2; column-gap: 10px; font-size: 9.5px; line-height: 1.33; }
  .serve-list li { break-inside: avoid; }
  .serve-list li::before { content: "• "; }

  .why { left: 20px; top: 318px; width: 250px; color: var(--paper); }
  .why .heading { color: var(--paper); font-size: 20px; margin-bottom: 5px; }
  .why p { font-size: 9.5px; font-style: italic; text-align: left; line-height: 1.35; }

  .contact { left: 410px; top: 18px; width: 345px; color: var(--royal); }
  .firm-name { font-family: var(--serif); font-weight: 600; font-size: 24px; line-height: 1.12; color: var(--royal); }
  .firm-tag { font-family: var(--head); font-weight: 600; font-size: 13px; letter-spacing: 1.5px; color: var(--ink); margin-top: 2px; }
  .site { font-family: var(--head); font-weight: 600; font-size: 21px; letter-spacing: 3px; margin-top: 9px; }
  .person { font-size: 11px; font-weight: 600; margin-top: 3px; text-transform: uppercase; }
  .contact-line { font-size: 10px; line-height: 1.33; }
  .office { font-family: var(--head); font-weight: 600; font-size: 17px; letter-spacing: 1px; margin-top: 7px; }

  .phones { left: 500px; top: 384px; color: var(--paper); font-weight: 700; font-size: 12px; line-height: 1.35; }
  .cover-name { left: 800px; top: 178px; width: 340px; text-align: center; }
  .cover-name .firm-name { color: var(--paper); font-size: 28px; }
  .cover-name .firm-tag { color: var(--paper); font-size: 15px; }
  .cover-phone { left: 773px; top: 398px; width: 387px; text-align: center; font-family: var(--head); font-weight: 600; font-size: 40px; line-height: 1; color: var(--paper); letter-spacing: 1px; }

  /* inside */
  .col { width: 343px; }
  .col .heading { font-size: 15px; margin: 6px 0 4px; }
  .col .heading:first-child { margin-top: 0; }
  .lead { font-size: 9px; color: var(--royal); font-weight: 600; margin-bottom: 4px; }
  .fee-list { list-style: none; font-size: 8.5px; line-height: 1.4; margin: 2px 0 4px 10px; }
  .fee-list li::before { content: "• "; }
  .col--one { left: 22px; top: 186px; }
  .col--two { left: 409px; top: 186px; }
  .col--three { left: 795px; top: 22px; }
</style>
</head>
<body>

<section class="spread spread--outside">
  <svg class="shapes" viewBox="0 0 1160 455" width="1160" height="455">
    <defs>
      <linearGradient id="fadeWhite" x1="0" y1="0" x2="1" y2="0">
        <stop offset="0" stop-color="#ffffff" stop-opacity=".55"/>
        <stop offset="1" stop-color="#ffffff" stop-opacity=".2"/>
      </linearGradient>
      <linearGradient id="cityTone" x1="0" y1="0" x2="0" y2="1">
        <stop offset="0" stop-color="#a9c4d6"/>
        <stop offset=".35" stop-color="#d8c7a0"/>
        <stop offset=".65" stop-color="#8a6a42"/>
        <stop offset="1" stop-color="#3d3128"/>
      </linearGradient>
      <radialGradient id="scalesTone" cx=".5" cy=".5" r=".6">
        <stop offset="0" stop-color="#c98a4e"/>
        <stop offset="1" stop-color="#5a2f17"/>
      </radialGradient>
    </defs>
    <rect x="387" y="0" width="386" height="455" fill="#d3d6dc" role="img" aria-label="Photo of classical courthouse columns, faded"/>
    <rect x="387" y="0" width="386" height="455" fill="url(#fadeWhite)"/>
    <rect x="773" y="0" width="387" height="455" fill="url(#cityTone)" role="img" aria-label="Photo of the New York City skyline at sunrise"/>
    <polygon points="640,0 1160,0 1160,34 1060,70 930,40" fill="var(--charcoal)"/>
    <polygon points="660,0 1160,0 1160,22 1050,56 930,28" fill="var(--royal)"/>
    <polygon points="0,282 387,350 387,364 0,296" fill="var(--charcoal)"/>
    <polygon points="0,296 387,364 387,455 0,455" fill="var(--royal)"/>
    <circle cx="318" cy="352" r="42" fill="url(#scalesTone)" stroke="#fff" stroke-width="4" role="img" aria-label="Photo of brass scales of justice"/>
    <polygon points="387,372 620,338 773,362 900,392 1010,362 1160,346 1160,455 387,455" fill="var(--royal)"/>
    <polygon points="387,390 620,356 773,380 900,410 1010,380 1160,364 1160,455 387,455" fill="var(--ink)"/>
    <line x1="387" y1="0" x2="387" y2="455" stroke="var(--fold)" stroke-width="1" opacity=".6"/>
    <line x1="773" y1="0" x2="773" y2="455" stroke="#000" stroke-width="1" opacity=".12"/>
    <circle cx="458" cy="412" r="18" fill="none" stroke="#fff" stroke-width="2"/>
    <rect x="451" y="400" width="14" height="24" rx="2.5" fill="none" stroke="#fff" stroke-width="2"/>
    <line x1="456" y1="419" x2="460" y2="419" stroke="#fff" stroke-width="2"/>
  </svg>

  <div class="block partner">
    <h2 class="heading">A Trusted Partner</h2>
    <p>We under the business of debt collection. Our primary focus is to help our clients secure the payments they are owed. We work closely with both private clients and leading service professionals, such as attorneys and accountants, to provide added value to their clients through customized debt collection services.</p>
    <p>We value our relationships as trusted advisors.</p>
    <div class="serve-title">We proudly serve:</div>
    <ul class="serve-list">
      <li>Law firms</li>
      <li>Accounting Firms</li>
      <li>Manufacturers</li>
      <li>Wholesalers and Distributors</li>
      <li>Collection Agencies</li>
      <li>Financial Service Companies</li>
      <li>Factors</li>
      <li>Doctors and Healthcare Professionals</li>
      <li>Carting Companies</li>
      <li>Oil Companies</li>
      <li>Freight Forwarders &amp; Custom Brokers</li>
      <li>Publishing and Advertising Companies</li>
      <li>Construction and Real Estate Firms</li>
    </ul>
  </div>

  <div class="block why">
    <h2 class="heading">Why Use Us</h2>
    <p>Anyone can sue a Debtor.</p>
    <p>It's not difficult to get nasty or to threaten those who owe you money in a rude manner.</p>
    <p>However, very few firms have the patience and experience to recover a Debt while keeping the relationship.</p>
  </div>

  <div class="block contact">
    <div class="firm-name">Marcus Dorven<br>&amp; Company, PLLC</div>
    <div class="firm-tag">DEBT COLLECTION ATTORNEYS</div>
    <div class="site">WWW.DORVENLAW.COM</div>
    <div class="person">Marcus J. Dorven, Esquire</div>
    <div class="contact-line">President<br>mdorven@dorvenlaw.com<br>(212) 555-0147 Cell</div>
    <div class="office">WESTCHESTER COUNTY OFFICE</div>
    <div class="contact-line">410 HARBOR RIDGE AVENUE, SUITE 12<br>WHITE PLAINS, NEW YORK 10601<br>(Near Exit 4 on the Parkway)</div>
    <div class="office">MAILING ADDRESS</div>
    <div class="contact-line">85 LINDELL STREET, SUITE 300<br>NEW YORK, NEW YORK 10010</div>
  </div>

  <div class="block phones">TOLL FREE: (877) 555-0190<br>LOCAL: (212) 555-0163<br>FAX: (917) 555-0128</div>

  <div class="block cover-name">
    <div class="firm-name">Marcus Dorven<br>&amp; Company, PLLC</div>
    <div class="firm-tag">DEBT COLLECTION ATTORNEYS</div>
  </div>
  <div class="block cover-phone">(877) 555-0190</div>
</section>

<section class="spread spread--inside">
  <svg class="shapes" viewBox="0 0 1160 455" width="1160" height="455">
    <defs>
      <linearGradient id="columnsTone" x1="0" y1="0" x2="1" y2="0">
        <stop offset="0" stop-color="#9a9a9a"/>
        <stop offset=".5" stop-color="#e6e6e6"/>
        <stop offset="1" stop-color="#7d7d7d"/>
      </linearGradient>
    </defs>
    <polygon points="0,0 740,0 300,186 0,100" fill="url(#columnsTone)" role="img" aria-label="Black and white photo of courthouse columns"/>
    <polygon points="0,0 70,0 0,130" fill="var(--ink)"/>
    <polygon points="0,96 300,180 730,0 762,0 300,204 0,120" fill="var(--royal)"/>
    <polygon points="0,432 210,455 0,455" fill="var(--royal)"/>
    <line x1="387" y1="0" x2="387" y2="455" stroke="#000" stroke-width="1" opacity=".1"/>
    <line x1="773" y1="0" x2="773" y2="455" stroke="#000" stroke-width="1" opacity=".1"/>
  </svg>

  <div class="block col col--one">
    <h2 class="heading">Who We Are</h2>
    <p><em>MARCUS DORVEN &amp; COMPANY, PLLC ("DORVEN")</em> is a New York based law firm devoted to the collection of accounts receivable and business debts.</p>
    <h2 class="heading">What We Do</h2>
    <p>Within 24 to 72 hours of receiving a claim, we will verify the debt, investigate the Debtor, skip trace all known stakeholders and file a lawsuit with the intent of collecting the full amount due in the shortest time possible.</p>
    <p>We will use all legal means necessary to locate, identify, seize, or otherwise garnish a Debtor's assets and income, while always having an attorney available to speak directly with the Debtor to achieve an amicable resolution as quickly as possible.</p>
    <h2 class="heading">Our Mission</h2>
    <p>Our mission is to protect our clients' bottom line, while preserving their reputation.</p>
    <p>We recognize and appreciate that your Debtor was once a trusted customer and may be a source of future revenue.</p>
    <p>We treat all Debtors with respect, while aggressively seeking to collect all monies owed.</p>
  </div>

  <div class="block col col--two">
    <h2 class="heading">Flexible Fee Structure</h2>
    <p>We recognize that each claim is unique, therefore to better serve our clients we offer a variety of fee structures that meet the needs of our clients. Including:</p>
    <ul class="fee-list">
      <li>Contingency Fee</li>
      <li>Flat Fee</li>
      <li>Hourly fee</li>
      <li>Monthly or Annual Retainer</li>
      <li>Any combination of the above</li>
    </ul>
    <h2 class="heading">Handling Medical Receivables</h2>
    <p>Medical receivables require a soft touch.</p>
    <p>Doctors and health organizations often write-off tens of thousands of dollars in unpaid deductibles and co-insurance which are rightfully due them out of fear that pursuing these debts will alienate, upset or offend their patients.</p>
    <p>We offer non-legal, HIPPA compliant collection methods which can effectively and consistently turn these otherwise uncollectible assets into real cash.</p>
    <p>Using a combination of letters and phone calls, our staff contacts patients in a professional and friendly manner to arrange for payments, as small as $15 per month, encouraging them to pay all monies owed.</p>
  </div>

  <div class="block col col--three">
    <h2 class="heading">Credit Advisory Services</h2>
    <div class="lead">How well do you really know your customers?</div>
    <p>As an added service to all of our clients, we will draft a customized credit application to be distributed to all of their customers.</p>
    <p>Working closely and alongside their salespeople, we will discreetly review and verify the customers' information and investigate all known stakeholders in order to determine creditworthiness.</p>
    <p>As your credit advisor, we will then make a meaningful recommendation with regard to the amount and terms credit should be offered to specific customers.</p>
    <p>Once a credit determination is made, we can provide the client with a credit agreement detailing each parties' obligations. Using such agreements minimizes risk, while enhancing our clients' professional stature with their customers.</p>
    <h2 class="heading">Keeping You In Compliance</h2>
    <p>As your collection attorney and advisor, we will assure that your collection practices are in full compliance with all applicable Federal and State laws, including The Fair Debt Collection Practices Act (FDCPA) and The Health Insurance Portability and Accountability Act (HIPPA).</p>
    <h2 class="heading">State-of-the-Art Technology</h2>
    <p>Our firm prides itself on utilizing the state-of-the-art technology in law office management, telephony, cyber security, document production, and cloud storage.</p>
    <p>Our clients can be assured that their critical business data is stored in a safe, secure, and confidential environment, while allowing us to seamlessly handle a large and ever growing book of business in a timely manner.</p>
  </div>
</section>

</body>
</html>
```